ZUMI 2020 Velko Cargo Runner

I want it to stand out and grab attention. I want it to follow the flow of our other designs and logo.

Requirements
Must have
• Our phone number, website, facets (Lighting Control, Automation, Audio/Video, Security Surveillance, Networking, Theater/Media Rooms)

```html
<!DOCTYPE html>
<html lang="en">
<head>
<meta charset="utf-8">
<title>Zumi Home Systems – Velko Cargo Runner Wrap</title>
<link rel="stylesheet" href="https://fonts.googleapis.com/css2?family=Oswald:wght@500;600;700&display=swap">
<style>
  :root {
    --page: #ffffff;
    --body-white: #f4f5f6;
    --wrap-dark: #333537;
    --wrap-blue: #2fa8dc;
    --trim-black: #1f2022;
    --glass: #d5d8db;
    --tyre: #1a1a1b;
    --hubcap: #b9bdc1;
    --pinstripe: #ffffff;
  }
  html, body {
    margin: 0;
    width: 1200px;
    height: 1200px;
    overflow: hidden;
    background: var(--page);
  }
  .wrap-sheet { display: block; width: 1200px; height: 1200px; }
  .van-body { fill: var(--body-white); stroke: #c9cccf; stroke-width: 1; }
  .wrap-dark { fill: var(--wrap-dark); }
  .wrap-blue { fill: var(--wrap-blue); }
  .pinstripe { fill: none; stroke: var(--pinstripe); stroke-width: 3; }
  .trim { fill: var(--trim-black); }
  .glass { fill: var(--glass); }
  .door-seam { fill: none; stroke: #9ea2a6; stroke-width: 1; }
  .wheel-arch { fill: var(--trim-black); }
  .tyre { fill: var(--tyre); }
  .hubcap { fill: var(--hubcap); }
  .hub-centre { fill: #5b6066; }
  .text { font-family: "Oswald", sans-serif; }
  .facet-list { font-size: 11.5px; font-weight: 600; fill: var(--trim-black); }
  .facet-dot { fill: var(--wrap-blue); }
  .brand-mark { font-size: 84px; font-weight: 700; fill: #ffffff; letter-spacing: 2px; }
  .brand-square { fill: var(--wrap-blue); }
  .company-name { font-size: 17px; font-weight: 700; fill: var(--wrap-blue); letter-spacing: 0.5px; }
  .tagline { font-size: 15px; font-weight: 600; fill: #ffffff; letter-spacing: 0.5px; }
  .website { font-size: 11px; font-weight: 600; fill: #ffffff; letter-spacing: 0.5px; }
  .phone { font-size: 26px; font-weight: 700; fill: var(--trim-black); letter-spacing: 0.5px; }
  .divider { stroke: var(--trim-black); stroke-width: 2.5; }
</style>
</head>
<body>
<svg class="wrap-sheet" viewBox="0 0 960 960" xmlns="http://www.w3.org/2000/svg">
  <defs>
    <g id="van-shell">
      <path class="van-body" d="M32,300 Q36,250 110,225 L245,122 Q272,96 330,94 L882,88 Q908,90 916,120 L928,330 Q930,372 906,374 L44,374 Q24,372 26,336 Z"/>
      <path class="wrap-dark" d="M668,92 L882,88 Q908,90 916,120 L928,330 Q930,372 906,374 L44,374 Q24,372 26,336 L34,282 L470,268 L612,262 Q636,258 640,232 Z"/>
      <path class="pinstripe" d="M34,280 L470,266 L612,260 Q634,256 638,232 L664,96"/>
      <path class="wrap-blue" d="M60,322 L926,290 L928,336 L80,384 Z"/>
      <path class="pinstripe" d="M60,316 L926,284"/>
      <path class="trim" d="M280,342 L690,332 L690,352 L280,364 Z"/>
      <path class="trim" d="M200,112 L245,122 L110,225 L72,232 Z"/>
      <path class="glass" d="M238,208 L290,140 Q300,130 320,130 L470,130 L470,236 L244,244 Z"/>
      <rect class="trim" x="26" y="352" width="904" height="22" rx="10"/>
      <circle class="wheel-arch" cx="185" cy="376" r="68"/>
      <circle class="wheel-arch" cx="778" cy="376" r="68"/>
      <circle class="tyre" cx="185" cy="378" r="60"/>
      <circle class="hubcap" cx="185" cy="378" r="44"/>
      <circle class="hub-centre" cx="185" cy="378" r="8"/>
      <circle class="tyre" cx="778" cy="378" r="60"/>
      <circle class="hubcap" cx="778" cy="378" r="44"/>
      <circle class="hub-centre" cx="778" cy="378" r="8"/>
    </g>
  </defs>

  <!-- Driver side -->
  <g class="van van-driver-side" transform="translate(0,-8)">
    <use href="#van-shell"/>
    <path class="door-seam" d="M482,128 L482,268 M482,300 L482,342 M690,258 L690,330"/>
    <g class="text facet-list">
      <circle class="facet-dot" cx="511" cy="136" r="2"/><text x="516" y="140">LIGHTING CONTROL</text>
      <circle class="facet-dot" cx="511" cy="152" r="2"/><text x="516" y="156">AUTOMATION</text>
      <circle class="facet-dot" cx="511" cy="168" r="2"/><text x="516" y="172">AUDIO/VIDEO</text>
      <circle class="facet-dot" cx="511" cy="184" r="2"/><text x="516" y="188">SECURITY SURVEILLANCE</text>
      <circle class="facet-dot" cx="511" cy="200" r="2"/><text x="516" y="204">NETWORKING</text>
      <circle class="facet-dot" cx="511" cy="216" r="2"/><text x="516" y="220">THEATER/MEDIA ROOMS</text>
    </g>
    <rect class="brand-square" x="698" y="124" width="18" height="18"/>
    <text class="text brand-mark" x="722" y="214">ZUMI</text>
    <text class="text company-name" x="700" y="250">ZUMI HOME SYSTEMS, LLC</text>
    <text class="text tagline" x="276" y="290">DREAM IT. AUTOMATE IT. LIVE IT.</text>
    <text class="text website" x="278" y="332">WWW.ZUMIHOMESYSTEMS.COM</text>
    <line class="divider" x1="494" y1="306" x2="494" y2="334"/>
    <text class="text phone" x="505" y="330">800-555-0142</text>
  </g>

  <!-- Passenger side -->
  <g class="van van-passenger-side" transform="translate(0,445)">
    <g transform="translate(960,0) scale(-1,1)">
      <use href="#van-shell"/>
    </g>
    <path class="door-seam" d="M478,128 L478,272 M478,300 L478,342 M264,330 L264,344"/>
    <rect class="brand-square" x="96" y="124" width="18" height="18"/>
    <text class="text brand-mark" x="120" y="214">ZUMI</text>
    <text class="text company-name" x="76" y="250">ZUMI HOME SYSTEMS, LLC</text>
    <g class="text facet-list">
      <circle class="facet-dot" cx="342" cy="136" r="2"/><text x="347" y="140">LIGHTING CONTROL</text>
      <circle class="facet-dot" cx="342" cy="152" r="2"/><text x="347" y="156">AUTOMATION</text>
      <circle class="facet-dot" cx="342" cy="168" r="2"/><text x="347" y="172">AUDIO/VIDEO</text>
      <circle class="facet-dot" cx="342" cy="184" r="2"/><text x="347" y="188">SECURITY SURVEILLANCE</text>
      <circle class="facet-dot" cx="342" cy="200" r="2"/><text x="347" y="204">NETWORKING</text>
      <circle class="facet-dot" cx="342" cy="216" r="2"/><text x="347" y="220">THEATER/MEDIA ROOMS</text>
    </g>
    <text class="text tagline" x="486" y="290">DREAM IT. AUTOMATE IT. LIVE IT.</text>
    <text class="text phone" x="274" y="324">800-555-0142</text>
    <line class="divider" x1="466" y1="302" x2="466" y2="330"/>
    <text class="text website" x="488" y="324">WWW.ZUMIHOMESYSTEMS.COM</text>
  </g>
</svg>
</body>
</html>
```